business card for LWR pty ltd

We require a business card that stands out . I have included our company flyer and would like the services listed to be put on the card so when we Give out the cards to customers they have an idea of services we provide. need the winning design to be in editable photo shop format, editable iMac pages format or editable windows publisher format, so that I can enter in names, email addresses, phone numbers etc myself. I have included a pdf documents of info / items needed on the card to use as reference please.
Updates

need more submissions

Need extra days to review

Sick

Target Market(s)

new customers

Contact Information for Business Card

details are on attached business card requirements file

Requirements
Must have
• I have attached a list of must haves

```html
<!DOCTYPE html>
<html lang="en">
<head>
<meta charset="utf-8">
<title>LWR pty ltd – Business Card</title>
<link rel="stylesheet" href="https://fonts.googleapis.com/css2?family=Jost:wght@400;500;600&family=Lato:wght@400&display=swap">
<style>
  :root {
    --canvas-bg: #bdbdbd;
    --mesh-dark: #0c0c0c;
    --mesh-mid: #2a2a2e;
    --band-light: #d9d9d9;
    --band-text: #262626;
    --logo-silver: #c4c4c8;
    --card-back-bg: #dcdcdc;
    --title-band: #111111;
    --title-text: #ffffff;
    --ink: #1b1b1b;
    --sky: #d6d6d6;
    --sand: #c98d4a;
    --sand-deep: #a9652c;
  }
  * { margin: 0; padding: 0; box-sizing: border-box; }
  html, body { width: 1200px; height: 728px; overflow: hidden; }
  body {
    background: var(--canvas-bg);
    position: relative;
    font-family: "Jost", sans-serif;
  }
  .card {
    position: absolute;
    top: 216px;
    width: 490px;
    height: 280px;
    overflow: hidden;
  }
  .card-front { left: 84px; }
  .card-back { left: 626px; background: var(--card-back-bg); }

  /* Front */
  .mesh-background {
    position: absolute; inset: 0;
    background: radial-gradient(ellipse at 50% 40%, var(--mesh-mid) 0%, var(--mesh-dark) 75%);
  }
  .brand-name {
    position: absolute;
    left: 0; right: 0; top: 52px;
    text-align: center;
    font-family: "Jost", sans-serif;
    font-weight: 600;
    font-size: 96px;
    line-height: 1;
    letter-spacing: 2px;
    color: var(--logo-silver);
  }
  .services-band {
    position: absolute;
    left: 0; right: 0; top: 201px; height: 52px;
    background: var(--band-light);
    display: flex; align-items: center; justify-content: center;
    padding: 0 22px;
  }
  .services-list {
    font-family: "Lato", sans-serif;
    font-size: 9.3px;
    line-height: 13.6px;
    color: var(--band-text);
    text-align: center;
  }

  /* Back */
  .company-band {
    position: absolute;
    left: 0; right: 0; top: 17px; height: 30px;
    background: var(--title-band);
    color: var(--title-text);
    font-weight: 600;
    font-size: 18px;
    letter-spacing: 1px;
    display: flex; align-items: center; justify-content: center;
  }
  .person-name {
    position: absolute; left: 0; right: 0; top: 59px;
    text-align: center;
    font-weight: 600;
    font-size: 15.5px;
    letter-spacing: 0.5px;
    color: var(--ink);
  }
  .person-role {
    position: absolute; left: 0; right: 0; top: 79px;
    text-align: center;
    font-size: 9.5px;
    color: var(--ink);
  }
  .contact-list {
    position: absolute; left: 146px; top: 100px;
    list-style: none;
  }
  .contact-item {
    display: flex; align-items: center;
    height: 19px;
    font-size: 12px;
    color: var(--ink);
  }
  .contact-item svg { width: 11px; height: 11px; margin-right: 8px; fill: var(--ink); }
  .fleet-photo {
    position: absolute;
    left: 0; right: 0; top: 186px; bottom: 0;
    background: linear-gradient(180deg, var(--sky) 0%, #b9a58a 30%, var(--sand) 60%, var(--sand-deep) 100%);
  }
</style>
</head>
<body>

<section class="card card-front">
  <div class="mesh-background" role="img" aria-label="Dark perforated hexagonal metal mesh texture"></div>
  <div class="brand-name">LWR</div>
  <div class="services-band">
    <p class="services-list">
      Over size loads/ Hot Shot Loads | Heavy Vehicle Recovery Services | Portable Water Deliveries | Road Building/<br>
      Maintenance | Earthworks | Sand &amp; Metal Supply &amp; Cartage | Road Train Tippers | Road Train Tankers |<br>
      Road Train Flat Tops | Drop Deck Trailers | Mine Site Accredited Equipment &amp; Operators
    </p>
  </div>
</section>

<section class="card card-back">
  <div class="company-band">LWR PTY LTD</div>
  <div class="person-name">DANIEL HARLOW</div>
  <div class="person-role">DIRECTOR</div>
  <div class="fleet-photo" role="img" aria-label="Road train with tipper trailers on an outback red dirt road"></div>
  <ul class="contact-list">
    <li class="contact-item">
      <svg viewBox="0 0 12 12"><path d="M6 0.5a4 4 0 0 0-4 4c0 3 4 7 4 7s4-4 4-7a4 4 0 0 0-4-4zm0 5.6a1.6 1.6 0 1 1 0-3.2 1.6 1.6 0 0 1 0 3.2z"/></svg>
      Lot 444 Example Address Australia
    </li>
    <li class="contact-item">
      <svg viewBox="0 0 12 12"><path d="M0.5 2.5h11v7h-11z M0.5 2.5l5.5 4 5.5-4" stroke="#dcdcdc" stroke-width="0.8"/></svg>
      email@lwrhaulage.com.au
    </li>
    <li class="contact-item">
      <svg viewBox="0 0 12 12"><path d="M3 1h2l0.6 2.4-1.2 0.9a6 6 0 0 0 3.3 3.3l0.9-1.2L11 7v2a1.5 1.5 0 0 1-1.5 1.5C5 10.5 1.5 7 1.5 2.5A1.5 1.5 0 0 1 3 1z"/></svg>
      000 444 000
    </li>
    <li class="contact-item">
      <svg viewBox="0 0 12 12"><circle cx="6" cy="6" r="5.2" fill="none" stroke="#1b1b1b" stroke-width="1"/><path d="M0.8 6h10.4M6 0.8c-2.6 2.8-2.6 7.6 0 10.4M6 0.8c2.6 2.8 2.6 7.6 0 10.4M1.8 3.5h8.4M1.8 8.5h8.4" fill="none" stroke="#1b1b1b" stroke-width="0.8"/></svg>
      www.websiteaddress.com
    </li>
  </ul>
</section>

</body>
</html>
```